Electrician Business needs flyer for discount offer and advertise services

Need a promotional flyer that will grab attention,, offer:

During the months of October & November receive a 10% discount on;
Ceiling fan installation
Smoke alarm installation
Replace existing downlights for new LED downlights.
Offer expires 30th November 2016
'Keep cool, stay safe and save power with VoltMate'

Would like to advertise services and quality on reverse-side. Can have graphic pointing to reverse side on both sides, encouraging customer to read both sides of flyer.
Contact details both sides
Design to suit two-sided A5

Reverse side list services;

All residential & commercial electrical services
Electrical contracting
Real estate/strata electrical maintenance & repairs
New builds
Renovations
Security sensor lighting
Ceiling fans
Smoke Alarms
Data connections

Target Market(s)

Residential home owners and commercial, building and construction companies

Industry/Entity Type

Electrical

Font styles to use
Serif

Colors
0255a3
ffffff

Requirements
Nice to have
• A picture of a modern ceiling fan.
• Arrow/graphic pointing to reverse side, so customer reads both sides of flyer

```html
<!DOCTYPE html>
<html lang="en">
<head>
<meta charset="utf-8">
<title>VoltMate Electrical Services – October &amp; November Offer</title>
<link href="https://fonts.googleapis.com/css2?family=Archivo+Black&family=Bebas+Neue&family=Lato:ital,wght@0,400;0,700;0,900;1,400;1,700&family=Oswald:wght@400;500&display=swap" rel="stylesheet">
<style>
  :root {
    --brand-blue: #0255a3;
    --deep-blue: #0a4a93;
    --brand-orange: #f0821e;
    --light-orange: #f7a55a;
    --ink: #111111;
    --slate: #5a5a5a;
    --white: #ffffff;
    --photo-light: #eeeeec;
    --photo-mid: #d9d6cf;
  }
  * { margin: 0; padding: 0; box-sizing: border-box; }
  html, body { width: 940px; height: 1200px; overflow: hidden; background: var(--white); }
  .flyer { position: relative; width: 940px; height: 1200px; overflow: hidden; background: var(--white); font-family: "Lato", sans-serif; }
  .flyer-shapes { position: absolute; inset: 0; }
  .brand { position: absolute; left: 560px; top: 36px; width: 330px; text-align: center; color: var(--white); }
  .brand-name { font-family: "Archivo Black", sans-serif; font-size: 44px; line-height: 1; letter-spacing: 1px; }
  .brand-tagline { font-family: "Lato", sans-serif; font-weight: 900; font-size: 17px; letter-spacing: 0.5px; margin-top: 4px; }
  .offer-expiry { position: absolute; left: 582px; top: 262px; color: var(--ink); }
  .offer-expiry-label { font-family: "Oswald", sans-serif; font-weight: 400; font-size: 40px; line-height: 1; letter-spacing: 0.5px; }
  .offer-expiry-date { font-family: "Bebas Neue", sans-serif; font-size: 58px; line-height: 1; margin-top: 6px; }
  .discount { position: absolute; left: 540px; top: 485px; width: 300px; text-align: center; }
  .discount-figure { font-family: "Bebas Neue", sans-serif; font-size: 150px; line-height: 0.9; color: var(--ink); }
  .discount-word { font-family: "Lato", sans-serif; font-weight: 400; font-size: 40px; line-height: 1; color: var(--ink); letter-spacing: 0.5px; }
  .discount-period { font-weight: 700; font-size: 19px; line-height: 1.3; color: var(--brand-blue); margin-top: 6px; }
  .headline { position: absolute; left: 38px; top: 786px; font-family: "Archivo Black", sans-serif; line-height: 1; }
  .headline-line { display: block; }
  .headline-keep { font-size: 62px; color: var(--slate); letter-spacing: 1px; }
  .headline-safe { font-size: 44px; color: var(--ink); margin-top: 8px; letter-spacing: 1px; }
  .headline-save { font-size: 47px; color: var(--brand-orange); margin-top: 8px; }
  .headline-brand { font-size: 67px; color: var(--brand-blue); margin-top: 6px; }
  .services { position: absolute; left: 553px; top: 813px; width: 380px; }
  .services-title { font-family: "Lato", sans-serif; font-size: 27px; color: var(--white); position: relative; height: 33px; line-height: 33px; padding-left: 20px; }
  .services-list { list-style: none; margin-top: 20px; }
  .services-list li { position: relative; padding-left: 39px; font-size: 17px; line-height: 1.2; color: #222; margin-bottom: 5px; }
  .services-list li::before { content: ""; position: absolute; left: 16px; top: 6px; width: 9px; height: 9px; border-radius: 50%; background: var(--brand-orange); }
  .contact { position: absolute; left: 40px; top: 1092px; color: var(--white); }
  .contact-phone { font-family: "Lato", sans-serif; font-style: italic; font-size: 38px; letter-spacing: 1.5px; line-height: 1; }
  .contact-links { display: flex; align-items: center; gap: 10px; margin-top: 12px; font-style: italic; font-weight: 700; font-size: 25px; }
  .contact-links svg { flex: none; }
</style>
</head>
<body>
<main class="flyer">
  <svg class="flyer-shapes" width="940" height="1200" viewBox="0 0 940 1200" aria-hidden="false">
    <defs>
      <linearGradient id="fan-photo-tone" x1="0" y1="0" x2="1" y2="1">
        <stop offset="0" stop-color="#f4f4f2"/>
        <stop offset="0.55" stop-color="#dcd3bd"/>
        <stop offset="1" stop-color="#efefed"/>
      </linearGradient>
      <radialGradient id="alarm-photo-tone" cx="0.5" cy="0.45" r="0.6">
        <stop offset="0" stop-color="#ffffff"/>
        <stop offset="1" stop-color="#cfcfcb"/>
      </radialGradient>
      <linearGradient id="bottom-band-tone" x1="0" y1="0" x2="1" y2="0">
        <stop offset="0" stop-color="#0a4a93"/>
        <stop offset="1" stop-color="#0255a3"/>
      </linearGradient>
    </defs>

    <!-- ceiling fan photo area -->
    <rect class="photo-fan" x="0" y="0" width="560" height="400" fill="url(#fan-photo-tone)" role="img" aria-label="Photo of a modern ceiling fan with wooden blades and a central light"/>

    <!-- header band -->
    <path class="header-accent" d="M380 0 H940 V137 H548 C530 100 470 30 380 0 Z" fill="var(--brand-orange)"/>
    <path class="header-band" d="M405 0 H940 V128 H538 C520 90 470 30 405 0 Z" fill="var(--brand-blue)"/>

    <!-- orange arc behind header on the left of the white panel -->
    <path class="panel-edge" d="M538 128 C560 180 555 300 520 400" fill="none" stroke="var(--brand-blue)" stroke-width="10"/>
    <path class="panel-edge-accent" d="M548 137 C572 190 566 300 532 400" fill="none" stroke="var(--brand-orange)" stroke-width="6"/>

    <!-- left swooshes -->
    <path class="swoosh-main" d="M0 435 C120 390 230 380 310 400 L300 450 C210 440 110 470 0 530 Z" fill="var(--brand-orange)"/>
    <path class="swoosh-lower" d="M0 555 C90 560 200 580 300 610 L320 640 C220 660 110 690 0 720 Z" fill="var(--brand-orange)"/>
    <path class="swoosh-fade" d="M0 720 C100 690 210 650 320 640 L330 665 C230 690 120 730 0 790 Z" fill="var(--light-orange)"/>

    <!-- smoke alarm photo circle -->
    <circle cx="388" cy="486" r="168" fill="var(--brand-blue)"/>
    <circle cx="388" cy="486" r="158" fill="var(--brand-orange)"/>
    <circle cx="388" cy="486" r="150" fill="url(#alarm-photo-tone)" role="img" aria-label="Photo of a white smoke alarm mounted on a ceiling"/>

    <!-- band behind discount badge -->
    <rect class="discount-band" x="800" y="522" width="140" height="165" fill="var(--brand-orange)"/>
    <line x1="820" y1="542" x2="940" y2="542" stroke="var(--white)" stroke-width="2" stroke-dasharray="2 3"/>
    <line x1="820" y1="667" x2="940" y2="667" stroke="var(--white)" stroke-width="2" stroke-dasharray="2 3"/>

    <!-- discount badge -->
    <circle cx="690" cy="605" r="160" fill="var(--brand-blue)"/>
    <circle cx="690" cy="605" r="146" fill="var(--white)"/>
    <circle cx="690" cy="605" r="140" fill="var(--brand-orange)"/>

    <!-- services divider -->
    <line x1="552" y1="783" x2="552" y2="1070" stroke="#333" stroke-width="2"/>
    <path class="services-tag" d="M553 813 H740 L760 829 L740 846 H553 Z" fill="var(--brand-blue)"/>

    <!-- footer band -->
    <path class="footer-accent" d="M0 1062 H500 L548 1108 H940 V1200 H0 Z" fill="var(--brand-orange)"/>
    <path class="footer-band" d="M0 1072 H492 L540 1118 H940 V1200 H0 Z" fill="url(#bottom-band-tone)"/>
    <path class="footer-corner" d="M800 1200 L940 1150 V1200 Z" fill="var(--brand-orange)"/>
  </svg>

  <header class="brand">
    <div class="brand-name">VoltMate</div>
    <div class="brand-tagline">Electrical Services</div>
  </header>

  <section class="offer-expiry">
    <p class="offer-expiry-label">OFFER EXPIRES</p>
    <p class="offer-expiry-date">30TH NOVEMBER 2016</p>
  </section>

  <section class="discount">
    <p class="discount-figure">10%</p>
    <p class="discount-word">DISCOUNT</p>
    <p class="discount-period">During the months of<br>October &amp; November</p>
  </section>

  <h1 class="headline">
    <span class="headline-line headline-keep">KEEP COOL</span>
    <span class="headline-line headline-safe">STAY SAFE AND</span>
    <span class="headline-line headline-save">SAVE POWER WITH</span>
    <span class="headline-line headline-brand">VOLTMATE</span>
  </h1>

  <section class="services">
    <h2 class="services-title">SERVICES:</h2>
    <ul class="services-list">
      <li>Electrical contracting</li>
      <li>Real estate/strata electrical maintenance<br>&amp; repairs</li>
      <li>New builds</li>
      <li>Renovations</li>
      <li>Security sensor lighting</li>
      <li>Ceiling fans</li>
      <li>Smoke Alarms</li>
      <li>Data connections</li>
    </ul>
  </section>

  <footer class="contact">
    <p class="contact-phone">CALL: 123 456 7890</p>
    <p class="contact-links">
      <svg width="30" height="22" viewBox="0 0 30 22" aria-hidden="true"><rect x="1" y="1" width="28" height="20" fill="none" stroke="var(--brand-orange)" stroke-width="2"/><path d="M1 1 L15 13 L29 1 M1 21 L11 10 M29 21 L19 10" fill="none" stroke="var(--brand-orange)" stroke-width="2"/></svg>
      <span>LOREM@lorem ipsum</span>
      <svg width="26" height="26" viewBox="0 0 26 26" aria-hidden="true"><g fill="none" stroke="var(--brand-orange)" stroke-width="2"><circle cx="13" cy="13" r="11"/><ellipse cx="13" cy="13" rx="5" ry="11"/><path d="M2 13 H24 M4 7 H22 M4 19 H22"/></g></svg>
      <span>www.lorem.com</span>
    </p>
  </footer>
</main>
</body>
</html>
```